Business Card Design for skin care range

The skincare range created here is a revolutionized skin care range that is very unique, natural and great for all skin types.The skincare range is cooled in nature, organic and rejuvenating for all skin types. 'Glow Tide Bloom' aims to radiate the vibe of wellness and harmony throughout our skin. The products are developed via bio-pharmaceutical high grade processes to put the life and radiance back in our skin.

Target Market(s)

All ages, as the skincare is great for all skin types.

Industry/Entity Type

Business

Contact Information for Business Card

M: 04 587 926 41 E: hello@velqorabeauty.com S: www.velqorabeauty.com

Font styles to use
Serif
Sans Serif
Script

Colors
0692cd

Requirements
Must have
• The business card we are aiming for is a simple yet elegant appeal with a black and white picture set in the middle of the business card (landscape orientation) with the caption "Glow Tide Bloom" centered spanning across the whole card horizontally. We are thinking having coloured (light-ish/ aqua coloured blue). we want the image encapsulated within a prestige/ mirror frame kind of border that is simply shown through the cutting out of the image. The remaining space on the card shall have a white background with a misty tonal fog that sweeps across the white.On the back of the card will be the text "Glow Tide Bloom" in the color blue being the hierarchical text. (same as the 'me' on the front).All other relevant contact information is in black. with also the statement "Keep me chilled" (as the products are to be refrigerated) in a different style so it is unique from the rest as its an important note. Also under the glow tide bloom text, i'd like to have the text "Bio-organic pharmaceutical grade skincare range" added to the card to emphasis the quality and uniqueness of the product. For the back of the card's background, the hazy tonal fog shall span across the whole backside of the card with the white background, keeping it plain and simple.
Nice to have
• Weare aiming for a professional elegant and classy look, with also that natural and joyful appeal.
• A black and white close up picture of a young persons face (preferably a girls face) to create the appeal of youth. The eyes must be of high importance. see the pictures we've uploaded and trial with them as we love the pictures of the girls faces

```html
<!DOCTYPE html>
<html lang="en">
<head>
<meta charset="utf-8">
<title>Glow Tide Bloom – Business Card</title>
<link rel="stylesheet" href="https://fonts.googleapis.com/css2?family=Cinzel:wght@400&family=Jost:wght@300&display=swap">
<style>
  :root {
    --page-bg: #e9e9ea;
    --card-white: #fbfbfc;
    --fog: #d9dadd;
    --fog-light: #eeeff1;
    --frame-line: #8f9095;
    --ornament: #b9babf;
    --brand-blue: #0692cd;
    --ink: #4a4a4f;
    --ink-soft: #707176;
    --photo-dark: #3e3d3c;
    --photo-mid: #8d8a86;
    --photo-light: #d4d2cf;
  }
  * { box-sizing: border-box; margin: 0; padding: 0; }
  html, body { width: 1200px; height: 1000px; overflow: hidden; }
  body { background: var(--page-bg); position: relative; }

  .card {
    position: absolute;
    left: 250px;
    width: 698px;
    height: 422px;
    overflow: hidden;
    background:
      radial-gradient(ellipse 60% 50% at 25% 30%, var(--fog-light), transparent 70%),
      radial-gradient(ellipse 55% 60% at 80% 75%, var(--fog), transparent 70%),
      radial-gradient(ellipse 70% 45% at 50% 95%, var(--fog-light), transparent 70%),
      linear-gradient(180deg, #f3f3f5 0%, var(--card-white) 45%, #ecedef 100%);
  }
  .card--front { top: 65px; }
  .card--back  { top: 515px; height: 420px; }

  .card__frame { position: absolute; inset: 0; width: 100%; height: 100%; }

  .corner-ornament {
    position: absolute;
    width: 62px; height: 62px;
    background: radial-gradient(circle, var(--ornament) 0%, rgba(185,186,191,0.35) 45%, transparent 72%);
  }
  .corner-ornament--tl { left: 22px;  top: 22px; }
  .corner-ornament--tr { right: 22px; top: 22px; }
  .corner-ornament--bl { left: 22px;  bottom: 22px; }
  .corner-ornament--br { right: 22px; bottom: 22px; }

  .front__stripes {
    position: absolute;
    left: 30px; right: 30px; top: 28px; bottom: 28px;
    background: linear-gradient(90deg, rgba(210,211,215,0.2), rgba(200,201,206,0.45) 30%, rgba(200,201,206,0.45) 70%, rgba(210,211,215,0.2));
  }
  .front__portrait {
    position: absolute;
    left: 200px; top: 0;
    width: 300px; height: 422px;
    background:
      radial-gradient(ellipse 38% 30% at 50% 42%, var(--photo-light), transparent 80%),
      radial-gradient(ellipse 55% 55% at 50% 35%, var(--photo-mid), transparent 85%),
      linear-gradient(180deg, var(--photo-dark) 0%, var(--photo-mid) 55%, #e6e5e3 100%);
    -webkit-mask-image: linear-gradient(90deg, transparent, #000 14%, #000 86%, transparent);
            mask-image: linear-gradient(90deg, transparent, #000 14%, #000 86%, transparent);
  }

  .brand-name {
    position: absolute;
    left: 0; right: 0;
    text-align: center;
    font-family: "Cinzel", "Times New Roman", serif;
    font-weight: 400;
    color: var(--brand-blue);
    white-space: nowrap;
  }
  .card--front .brand-name { top: 318px; font-size: 50px; letter-spacing: 1px; }
  .card--back  .brand-name { top: 76px;  font-size: 56px; letter-spacing: 1px; }

  .back__tagline {
    position: absolute;
    left: 0; right: 0; top: 172px;
    text-align: center;
    font-family: "Jost", "Helvetica Neue", sans-serif;
    font-weight: 300;
    font-size: 19px;
    color: var(--ink-soft);
  }
  .back__notice {
    position: absolute;
    left: 0; right: 0; top: 208px;
    text-align: center;
    font-family: "Cinzel", "Times New Roman", serif;
    font-size: 27px;
    color: var(--ink);
  }
  .back__notice-accent { color: var(--brand-blue); }

  .contact-list {
    position: absolute;
    left: 0; right: 0; top: 274px;
    list-style: none;
    text-align: center;
    font-family: "Jost", "Helvetica Neue", sans-serif;
    font-weight: 300;
    font-size: 23px;
    line-height: 34px;
    color: var(--ink-soft);
  }
  .contact-list__label {
    font-family: "Cinzel", "Times New Roman", serif;
    color: var(--brand-blue);
    font-size: 21px;
  }
</style>
</head>
<body>

  <section class="card card--front" aria-label="Business card front">
    <div class="front__stripes" role="img" aria-label="Soft silver vertical stripes with snowflake mist"></div>
    <div class="front__portrait" role="img" aria-label="Black and white close-up portrait of a young girl, eyes in focus"></div>
    <svg class="card__frame" viewBox="0 0 698 422" aria-hidden="true">
      <rect x="30" y="28" width="638" height="366" fill="none" stroke="var(--frame-line)" stroke-width="1"/>
    </svg>
    <div class="corner-ornament corner-ornament--tl" role="img" aria-label="Silver filigree corner ornament"></div>
    <div class="corner-ornament corner-ornament--tr" role="img" aria-label="Silver filigree corner ornament"></div>
    <div class="corner-ornament corner-ornament--bl" role="img" aria-label="Silver filigree corner ornament"></div>
    <div class="corner-ornament corner-ornament--br" role="img" aria-label="Silver filigree corner ornament"></div>
    <h1 class="brand-name">Glow Tide Bloom</h1>
  </section>

  <section class="card card--back" aria-label="Business card back">
    <svg class="card__frame" viewBox="0 0 698 420" aria-hidden="true">
      <rect x="30" y="28" width="638" height="364" fill="none" stroke="var(--frame-line)" stroke-width="1"/>
    </svg>
    <div class="corner-ornament corner-ornament--tl" role="img" aria-label="Silver filigree corner ornament"></div>
    <div class="corner-ornament corner-ornament--tr" role="img" aria-label="Silver filigree corner ornament"></div>
    <div class="corner-ornament corner-ornament--bl" role="img" aria-label="Silver filigree corner ornament"></div>
    <div class="corner-ornament corner-ornament--br" role="img" aria-label="Silver filigree corner ornament"></div>
    <h2 class="brand-name">Glow Tide Bloom</h2>
    <p class="back__tagline">Bio-organic Pharmaceutical Grade Skincare Range</p>
    <p class="back__notice">KEEP ME <span class="back__notice-accent">CHILLED</span></p>
    <ul class="contact-list">
      <li><span class="contact-list__label">M:</span> 04 587 926 41</li>
      <li><span class="contact-list__label">E:</span> hello@velqorabeauty.com</li>
      <li><span class="contact-list__label">S:</span> www.velqorabeauty.com</li>
    </ul>
  </section>

</body>
</html>
```